Business Card Design

I am a video director/cameraman and photographer. I cover documentaries, corporate, government departments, educational and non profits. They could be on Tv, Vidflo or DVD to 10 or 10 thousand ppl. Some have been seen worldwide and won international awards.
I regard myself as bold and saturated...as in I want strong ideas of substance to come through in a film and that the info is valid, interesting and saturates the mind without it being geeky boring.
Need a great logo and layout for cards. My name is Barnaby Tolliver and my company is RT Media Productions.

Must have company name, my name, email, website, phone and type of films I do. I'll supply additional info for the back- which will be companies I have filmed for.

Attach image shows I like the boxes/icons idea but am open to yr ideas...Roar on!
Updates

Reason: I am charged by your designs. This is the first time I have used ths type of service and getting to know you guys is very good value for me. Please keep your creative spirit in this. I want a contemporary logo. Some have shown the way forward and a few need to show a clean, current looking image of my attitude by way of log and design. Thx to you all Barn

Industry/Entity Type

Government

```html
<!DOCTYPE html>
<html lang="en">
<head>
<meta charset="utf-8">
<title>RT Media Productions – Business Card</title>
<link rel="stylesheet" href="https://fonts.googleapis.com/css2?family=Lato:wght@400;700;900&display=swap">
<style>
  :root {
    --card-dark: #262626;
    --pattern-dark: #232323;
    --accent: #f28a30;
    --white: #ffffff;
    --page: #e9e6e1;
  }
  * { box-sizing: border-box; margin: 0; padding: 0; }
  html, body { width: 1200px; height: 1000px; overflow: hidden; }
  body {
    background: var(--page);
    font-family: "Lato", Arial, sans-serif;
    position: relative;
  }
  .card {
    position: absolute;
    left: 200px;
    width: 800px;
    height: 455px;
    background: var(--card-dark);
    overflow: hidden;
    box-shadow: 0 6px 18px rgba(0,0,0,0.18);
  }
  .card--back { top: 30px; }
  .card--front { top: 515px; }

  .back-pattern {
    position: absolute;
    inset: 0;
    background: linear-gradient(135deg, #2a2a2a, var(--pattern-dark));
  }
  .back-brand {
    position: absolute;
    left: 470px;
    top: 190px;
    display: flex;
    align-items: center;
    gap: 16px;
  }
  .brand-square {
    width: 72px;
    height: 72px;
    background: var(--accent);
    flex: none;
  }
  .brand-name {
    color: var(--accent);
    font-weight: 900;
    font-size: 26px;
    letter-spacing: 1px;
    text-transform: uppercase;
    line-height: 1.1;
  }

  .front-brand {
    position: absolute;
    left: 60px;
    top: 48px;
    display: flex;
    align-items: center;
    gap: 24px;
  }
  .front-brand .brand-square { width: 112px; height: 112px; }
  .front-brand .brand-name { font-size: 38px; }

  .person {
    position: absolute;
    left: 60px;
    top: 200px;
  }
  .person-name {
    color: var(--accent);
    font-weight: 700;
    font-size: 25px;
    line-height: 1.2;
  }
  .person-role {
    color: var(--white);
    font-size: 21px;
    line-height: 1.2;
    margin-top: 2px;
  }

  .contacts {
    position: absolute;
    left: 60px;
    top: 296px;
    list-style: none;
  }
  .contacts li {
    display: flex;
    align-items: center;
    gap: 10px;
    color: var(--white);
    font-size: 20px;
    line-height: 1;
    height: 29px;
  }
  .contacts svg { width: 20px; height: 20px; flex: none; }

  .stripe {
    position: absolute;
    left: 0; right: 0; bottom: 0;
    height: 18px;
    display: flex;
  }
  .stripe-accent { width: 40%; background: var(--accent); }
  .stripe-light { flex: 1; background: var(--white); }
</style>
</head>
<body>
  <section class="card card--back" aria-label="Card back">
    <div class="back-pattern" role="img" aria-label="Dark tonal pattern of repeated square motifs"></div>
    <div class="back-brand">
      <div class="brand-square"></div>
      <div class="brand-name">RT Media<br>Productions</div>
    </div>
  </section>

  <section class="card card--front" aria-label="Card front">
    <div class="front-brand">
      <div class="brand-square"></div>
      <div class="brand-name">RT Media<br>Productions</div>
    </div>

    <div class="person">
      <p class="person-name">Barnaby Tolliver</p>
      <p class="person-role">Video Director | Cameraman | Photographer</p>
    </div>

    <ul class="contacts">
      <li>
        <svg viewBox="0 0 20 20" aria-hidden="true"><path fill="var(--accent)" d="M4 2l3 1 1 4-2 1.5c1 2.2 2.6 3.8 4.5 4.5L12 11l4 1 1 3-2 2.5C8.5 17 3 11.5 2.5 5z"/></svg>
        123 456 7890
      </li>
      <li>
        <svg viewBox="0 0 20 20" aria-hidden="true"><rect x="5" y="2" width="10" height="16" rx="2" fill="none" stroke="var(--accent)" stroke-width="2"/><rect x="7" y="5" width="6" height="6" fill="var(--accent)"/></svg>
        123 456 7890
      </li>
      <li>
        <svg viewBox="0 0 20 20" aria-hidden="true"><rect x="2" y="4" width="16" height="12" fill="var(--accent)"/><path d="M2 4l8 7 8-7" fill="none" stroke="var(--card-dark)" stroke-width="1.5"/></svg>
        barnaby@rtmediaproductions.com
      </li>
      <li>
        <svg viewBox="0 0 20 20" aria-hidden="true"><circle cx="10" cy="10" r="8" fill="none" stroke="var(--accent)" stroke-width="2"/><ellipse cx="10" cy="10" rx="3.5" ry="8" fill="none" stroke="var(--accent)" stroke-width="1.5"/><path d="M2 10h16" stroke="var(--accent)" stroke-width="1.5"/></svg>
        www.rtmediaproductions.com
      </li>
    </ul>

    <div class="stripe">
      <div class="stripe-accent"></div>
      <div class="stripe-light"></div>
    </div>
  </section>
</body>
</html>
```